Flyer for American Indian Elders on Dementia Warning Signs

We need a flyer designed for older adults who are American Indian or Alaska Native (in the U.S.).

Ideally, the flyer should complement the colors of our logos. The project logo and our organization logo are attached to the brief.

When people see the flyer we want them to feel that it represents their culture, is warm, and professional but relatable to older adults and people who have limited incomes.

I have attached an earlier draft of the document we designed ourselves BUT we want different and better.

It is for older adults who have trouble reading so:
1. you must use a font that is 11.5 points or larger
2. Do not put text over complex pictures or use shading with words
3. You can use a serif font for the heading, but should use san serif for the body text
4. There should be good contrast between the font color and background

Please do not use any images that include a head dress or pictures of American Indian people or things that are very traditional or "token" imagery.

We need to save a small space under the call out box/ somewhere on the flyer for other people to add their logo once they download.

Let us know if you have questions or need additional information.

Target Market(s)

Older American Indian people

Font styles to use
Serif
Sans Serif

Requirements
Must have
• Easy to read for older adults
Should not have
• indian headdress

```html
<!DOCTYPE html>
<html lang="en">
<head>
<meta charset="utf-8">
<title>10 Signs of Thinking or Memory Changes that Might be Dementia</title>
<link href="https://fonts.googleapis.com/css2?family=Roboto+Condensed:wght@400;700&display=swap" rel="stylesheet">
<style>
:root{
  --clay:#b0605a;
  --ink:#111;
  --navy:#0b1a33;
  --mist:#c9dde0;
  --haze:#e9eff1;
  --teal:#4fa3ab;
  --rose:#b86a60;
  --slot:#dce6ea;
  --slot-text:#8a9aa3;
  --white:#fff;
}
*{margin:0;padding:0;box-sizing:border-box}
html,body{width:927px;height:1200px;overflow:hidden;background:var(--white)}
body{font-family:"Roboto Condensed",Arial,sans-serif;color:var(--ink);position:relative}
.masthead{position:absolute;left:0;top:0;width:927px;height:151px;background:var(--clay)}
.masthead-rule{position:absolute;left:0;top:152px;width:927px;height:15px;background:#000}
.signpost{position:absolute;left:0;top:0}
.big-ten{position:absolute;left:36px;top:30px;font-weight:700;font-size:124px;letter-spacing:-10px;color:var(--white);line-height:1}
.signs-word{position:absolute;left:152px;top:66px;font-weight:700;font-size:50px;color:var(--white);line-height:1}
.title{position:absolute;left:363px;top:26px;color:var(--white);font-weight:700;line-height:1}
.title .l1{font-size:39px;display:block}
.title .l2{font-size:36px;display:block;margin-top:4px}
.title .l2 b{font-size:57px}
.intro{position:absolute;left:0;top:168px;width:927px;height:65px;background:var(--mist);font-size:18.5px;line-height:23px;padding:10px 48px;text-align:left}
.risk{position:absolute;left:0;top:233px;width:927px;height:66px;background:var(--haze);font-weight:700;font-size:19px;line-height:28px;text-align:center;padding-top:6px}
.risk .ask{font-size:21.5px}
.sign{position:absolute;width:420px}
.sign .num{position:absolute;left:-42px;top:-2px;width:37px;height:37px;border-radius:50%;background:linear-gradient(180deg,var(--teal),var(--rose));color:var(--white);font-weight:700;font-size:28px;text-align:center;line-height:38px}
.sign h2{font-weight:700;font-size:20.5px;line-height:25px}
.sign p,.sign li{font-size:18px;line-height:23.6px}
.sign ul{list-style:none}
.sign li{padding-left:13px;position:relative}
.sign li::before{content:"•";position:absolute;left:0}
.sign .wrap{padding-left:0;text-indent:0}
.sign .wrap::before{content:""}
.callout-tab{position:absolute;left:41px;top:875px;width:397px;height:60px;background:var(--navy);border-radius:18px 18px 0 0}
.brand{position:absolute;left:22px;top:14px;display:flex;align-items:center;gap:10px;color:var(--teal);font-weight:700;font-size:17px;line-height:19px}
.brand .dot{width:30px;height:30px;border-radius:50%;background:var(--teal);flex:none}
.callout{position:absolute;left:0;top:923px;width:927px;height:140px;background:var(--navy);color:var(--white);padding:38px 0 0 40px}
.callout li{list-style:none;font-size:17.5px;line-height:24.4px;display:flex;align-items:center;gap:6px}
.callout svg{flex:none}
.footer-org{position:absolute;left:48px;top:1090px;width:130px;color:var(--rose);font-weight:700;font-size:15px;line-height:18px}
.footer-org .mark{display:block;width:44px;height:44px;background:var(--teal);margin-bottom:8px}
.learn{position:absolute;left:202px;top:1076px;font-size:17.5px;line-height:23px}
.learn a{display:block;color:var(--navy);font-weight:700;font-size:22px;line-height:28px;text-decoration:none}
.learn a:first-of-type{margin-top:4px}
.logo-slot{position:absolute;left:616px;top:1075px;width:282px;height:104px;background:var(--slot);color:var(--slot-text);font-size:22px;display:flex;align-items:center;justify-content:center}
</style>
</head>
<body>
<header>
  <div class="masthead"></div>
  <svg class="signpost" width="360" height="168" viewBox="0 0 360 168" aria-hidden="true">
    <path d="M188 29 H314 L346 60 L314 92 H188 Z" fill="none" stroke="#000" stroke-width="13" stroke-linejoin="round"/>
    <rect x="230" y="120" width="20" height="48" fill="#000"/>
    <rect x="142" y="60" width="156" height="77" rx="18" fill="#000"/>
  </svg>
  <div class="big-ten">10</div>
  <div class="signs-word">Signs</div>
  <h1 class="title"><span class="l1">of Thinking or Memory Changes</span><span class="l2">that <b>Might be Dementia</b></span></h1>
  <div class="masthead-rule"></div>
</header>

<p class="intro">As we get older, we may slow down a bit. This is a normal part of aging. Changes in memory or thinking that make it harder to get through the day, are not a normal part of aging. These may be early signs of dementia.</p>
<p class="risk">Because American Indian and Alaska Native people have a high risk of dementia, it is important<br>to know the warning signs. <span class="ask">Do you have any of these 10 signs? If so, talk to your doctor.</span></p>

<main>
  <section class="sign" style="left:75px;top:316px">
    <span class="num">1</span>
    <h2>Memory loss that affects your daily life.</h2>
    <p>You may:</p>
    <ul><li>Forget events or important dates</li><li>Repeat yourself</li><li>Rely more often on lists or sticky notes to</li><li class="wrap">remember things</li></ul>
  </section>
  <section class="sign" style="left:75px;top:469px">
    <span class="num">2</span>
    <h2>Trouble planning or solving problems.</h2>
    <p>You may have a harder time:</p>
    <ul><li>Paying bills</li><li>Cooking recipes you have used for years</li></ul>
  </section>
  <section class="sign" style="left:75px;top:573px">
    <span class="num">3</span>
    <h2>Get confused about the<br>time, date, or where you are.</h2>
  </section>
  <section class="sign" style="left:75px;top:637px">
    <span class="num">4</span>
    <h2>Daily tasks are getting harder,</h2>
    <p>Including:</p>
    <ul><li>Driving</li><li>Making a grocery list or going shopping</li></ul>
  </section>
  <section class="sign" style="left:75px;top:745px">
    <span class="num">5</span>
    <h2>Trouble with how your eyesight and<br>thinking work together that gets worse.</h2>
    <p>This includes:</p>
    <ul><li>Tripping, falls, or problems with your balance</li><li>Spilling or dropping things more</li></ul>
  </section>

  <section class="sign" style="left:506px;top:316px">
    <span class="num">6</span>
    <h2>New trouble talking or writing.</h2>
    <p style="margin-top:5px">You have a hard time finding the words you want to say. For example, you may say “that thing on your wrist that tells time” instead of “watch.”</p>
  </section>
  <section class="sign" style="left:506px;top:433px">
    <span class="num">7</span>
    <h2>Lose and cannot find things.</h2>
    <p style="margin-top:5px">For example, you:</p>
    <ul><li>Can’t find the coffee pot that you use every day</li><li>Might put your car keys in the freezer</li></ul>
  </section>
  <section class="sign" style="left:506px;top:542px">
    <span class="num">8</span>
    <h2>Notice changes in mood or personality</h2>
    <p style="margin-top:5px">Such as being:</p>
    <ul><li>Easily mad or sad in everyday situations</li><li>More fearful (scared) or suspicious (not trusting)</li></ul>
  </section>
  <section class="sign" style="left:506px;top:653px;width:410px">
    <span class="num">9</span>
    <h2>Act different and make poor choices.</h2>
    <p style="margin-top:5px">This may make you more likely to:</p>
    <ul><li>Spend money you do not have or be a scam victim</li><li>Stop washing up regularly or pay less attention to how you look</li><li>Forget to take care of your pet</li></ul>
  </section>
  <section class="sign" style="left:506px;top:814px;width:400px">
    <span class="num">10</span>
    <h2>Pull away from friends and family because it<br>is harder to keep up.</h2>
    <p style="margin-top:3px">You may not want to do things you used to enjoy, like sporting events, church, music, or sex.</p>
  </section>
</main>

<div class="callout-tab">
  <div class="brand"><span class="dot"></span><span>Native Elders<br>Brain Health Center</span></div>
</div>
<aside class="callout">
  <ul>
    <li><svg width="16" height="16" viewBox="0 0 16 16"><path d="M2 9 L6 13 L14 2" fill="none" stroke="#4fa3ab" stroke-width="3"/></svg>American Indian and Alaska Native people have a high risk of dementia.</li>
    <li><svg width="16" height="16" viewBox="0 0 16 16"><path d="M2 9 L6 13 L14 2" fill="none" stroke="#4fa3ab" stroke-width="3"/></svg>Big changes in memory or thinking that make it hard to get through the day are not a normal part of aging.</li>
    <li><svg width="16" height="16" viewBox="0 0 16 16"><path d="M2 9 L6 13 L14 2" fill="none" stroke="#4fa3ab" stroke-width="3"/></svg>People with one or more of these 10 signs should talk to their doctor to find the cause. It is not always dementia.</li>
    <li><svg width="16" height="16" viewBox="0 0 16 16"><path d="M2 9 L6 13 L14 2" fill="none" stroke="#4fa3ab" stroke-width="3"/></svg>Early dementia diagnosis gives you a chance to get care and plan your future.</li>
  </ul>
</aside>

<footer>
  <div class="footer-org"><span class="mark"></span>Council for Indigenous Elder Wellness</div>
  <div class="learn">To learn more about the warning signs of dementia<br>in American Indian and Alaska Native people, visit:
    <a>www.EldersBrainCenter.org</a>
    <a>www.healthyagingnet.org/aging</a>
  </div>
  <div class="logo-slot">Logo space</div>
</footer>
</body>
</html>
```